Organic Food Producer Needs Business Card

We need an attractive business card that is both trendy and professional. We are a FQRB, Vetra Clear Certified organic producer of coconut oil, coconut flour and additional cacao products. We produce some of the world's purest coconut oil and coconut oil derived products in the world.
We take pride in the purity of our products and the transparency with which we create our products. Use of FQRB Organic and Vetra Clear logos is acceptable and preferred. The final design would reflect our values for purity and the natural state of our products.
The business card should include: job title, email address, phone number and facebook, twitter, instagram tag.
Don't be afraid to get creative! I have attached some of our packaging design in JPG format as well as our logo. The jpgs dont display the colors correctly in chrome but they will display correctly if you DL and open them in photoshop.
Target Market(s)
Cards likely to be used in organic food industry events for people such as buyers, trade show reps, etc... but also store owners and people casually interested in.
The company's target market :
Primary:
Women - 22-65. Women typically hold the household budget and make the purchasing decisions at the supermarket. They are interested in quality healthy and beauty products at a good value. Organic, fair trade, artisanally made are all important attributes of brands they purchase. They try to maintain a healthy lifestyle through proper eating, exercise and work/life balance.
Secondary:
Men - 44% of American adults are single so it is important to note that men will also be a key target audience. And they too are concerned and passionate about organic, fair trade, artisanally made, good value and living a healthy lifestyle.
Tertiary:
Health & Wellness Professionals (Nutritionists, Doctors, etc) Coconut is highly nutritional and more and more, it is being recommended as part of a healthy diet by professionals. We should keep this audience in mind as well, particularly when we build a website with useful resources such as the company’s high standards, the health benefits of coconut, nutrition info and recipes.
Industry/Entity Type
Business
Requirements
Must have
- Pretty open minded about creativity and variety, I do like the color palettes in the labeling files provided... but it is not a deal breaker to vary from this.
Should be visually impacting.
Nice to have
- Would like to have some creative use of raised lettering or detail.
Should not have
- Although the company is based in the caribbean, we are not looking for an overly ethnic caribbean feel.
You should open the attached files in photoshop, as they seem to distort the color in a web browser.

```html
<!DOCTYPE html>
<html lang="en">
<head>
<meta charset="utf-8">
<title>Clear Husk – Business Card</title>
<link rel="stylesheet" href="https://fonts.googleapis.com/css2?family=Open+Sans:wght@400;600;700&display=swap">
<style>
  :root {
    --page: #eeeae4;
    --brown: #231412;
    --cream: #fdd29b;
    --teal: #117184;
    --ink: #231412;
  }
  * { box-sizing: border-box; margin: 0; padding: 0; }
  html, body {
    width: 1200px; height: 1000px; overflow: hidden;
    background: var(--page);
    font-family: "Open Sans", Arial, sans-serif;
    color: var(--ink);
  }
  .canvas { position: relative; width: 1200px; height: 1000px; }
  .card {
    position: absolute; left: 250px; width: 700px; height: 400px;
    border-radius: 34px; overflow: hidden;
    box-shadow: 0 6px 18px rgba(0,0,0,.18);
  }

  /* Front */
  .card-front { top: 70px; background: var(--brown); }
  .card-front .footer-band {
    position: absolute; left: 0; right: 0; bottom: 0; height: 58px;
    background: var(--cream);
  }
  .card-front .website {
    position: absolute; left: 0; right: 0; bottom: 70px;
    text-align: center; color: var(--cream);
    font-size: 17px; letter-spacing: .5px;
  }
  .brand-lockup {
    position: absolute; left: 0; right: 0; top: 110px;
    display: flex; flex-direction: column; align-items: center; gap: 8px;
  }
  .brand-lockup .mark {
    width: 58px; height: 58px; border-radius: 50%;
    background: var(--teal);
  }
  .brand-lockup .brand-name {
    font-size: 54px; font-weight: 600; color: var(--cream);
    line-height: 1; letter-spacing: 1px;
  }
  .brand-lockup .tagline {
    font-size: 18px; color: var(--cream); letter-spacing: 1px;
  }

  /* Back */
  .card-back { top: 530px; background: var(--cream); }
  .card-back .stripe {
    position: absolute; top: 0; bottom: 0; left: 88px; width: 170px;
    background: var(--brown);
  }
  .card-back .emblem {
    position: absolute; left: 70px; top: 100px; width: 200px; height: 200px;
    border-radius: 50%; background: var(--teal);
    border: 8px solid var(--cream);
  }
  .card-back .company {
    position: absolute; left: 300px; top: 88px;
    font-size: 34px; font-weight: 700; letter-spacing: .5px;
  }
  .card-back .person {
    position: absolute; left: 290px; top: 200px; width: 190px; text-align: right;
  }
  .person .name { font-size: 26px; font-weight: 700; line-height: 1.15; white-space: nowrap; }
  .person .title { font-size: 24px; line-height: 1.15; }
  .card-back .divider {
    position: absolute; left: 496px; top: 158px; width: 2px; height: 104px;
    background: var(--ink);
  }
  .contacts {
    position: absolute; left: 510px; top: 160px; width: 175px;
    font-size: 15px; line-height: 1.7;
  }
  .contacts li { list-style: none; display: flex; align-items: center; gap: 6px; white-space: nowrap; }
  .contacts svg { width: 14px; height: 14px; flex: none; }
  .contacts .social-mark { width: 12px; height: 12px; background: var(--ink); border-radius: 2px; flex: none; }
  .card-back .tagline {
    position: absolute; left: 300px; top: 300px;
    font-size: 17px; letter-spacing: .3px;
  }
</style>
</head>
<body>
<main class="canvas">
  <section class="card card-front">
    <div class="brand-lockup">
      <div class="mark"></div>
      <div class="brand-name">clear husk</div>
      <div class="tagline">handcrafted in the caribbean</div>
    </div>
    <div class="website">WWW.YOURWEB.COM</div>
    <div class="footer-band"></div>
  </section>

  <section class="card card-back">
    <div class="stripe"></div>
    <div class="emblem"></div>
    <h1 class="company">CLEAR HUSK</h1>
    <div class="person">
      <div class="name">NAME HERE</div>
      <div class="title">JOB TITLE</div>
    </div>
    <div class="divider"></div>
    <ul class="contacts">
      <li>
        <svg viewBox="0 0 16 16" aria-hidden="true"><rect x="4" y="1" width="8" height="14" rx="1.5" fill="none" stroke="#231412" stroke-width="1.6"/><circle cx="8" cy="12.3" r=".9" fill="#231412"/></svg>
        12345678910
      </li>
      <li>
        <svg viewBox="0 0 16 16" aria-hidden="true"><rect x="1" y="3" width="14" height="10" fill="none" stroke="#231412" stroke-width="1.6"/><path d="M1 3l7 6 7-6" fill="none" stroke="#231412" stroke-width="1.6"/></svg>
        youremail@here.com
      </li>
      <li><span class="social-mark"></span>@clearhusk</li>
    </ul>
    <p class="tagline">HANDCRAFTED IN THE CARIBBEAN</p>
  </section>
</main>
</body>
</html>
```